Harlow Stonefield Civil Construction website design

We want a Bold website to promote our Heavy Civil Construction company, We would like an organic / tangible feel to the site. The pictures will be over saturated so they pop. We need to be able to easliy upload new projects and pictures on a regular basis.
Home page will have a full screen width image, "home page image" with silhouette and logo. It will also have about us area and picture
Page 2 will be Project Gallery with pictures in project folders
Page 3 will be an employment application form and submission
Page 4 will be Contact Us
Target Market(s)
Construction indusrty
Industry/Entity Type
Contractor
Coding
Coded - Design and coding required
Number of Pages Required
4 page
Font styles to use
Other font styles liked:
- Hypatia Sans Pro Light
Look and feel

```html
<!DOCTYPE html>
<html lang="en">
<head>
<meta charset="utf-8">
<title>Harlow Stonefield Civil Construction — Website</title>
<link href="https://fonts.googleapis.com/css2?family=Cabin:wght@400;500;600;700&family=Montserrat:wght@600;700;800&display=swap" rel="stylesheet">
<style>
:root{
  --blue:#3a55a8;
  --blue-deep:#2b4291;
  --navy:#1f2b4d;
  --ink:#222633;
  --muted:#6b6f7a;
  --paper:#ffffff;
  --mist:#f2f2f3;
  --board:#e9eaee;
  --night:#1b1e26;
  --line:#d6d8de;
}
*{box-sizing:border-box;margin:0;padding:0}
html,body{width:1200px;height:3000px;overflow:hidden}
body{background:var(--board);font-family:"Cabin",sans-serif;color:var(--ink);position:relative}
.site{position:absolute;top:385px;background:var(--paper);overflow:hidden;box-shadow:0 6px 30px rgba(20,30,60,.18)}
.site-desktop{left:20px;width:820px}
.site-mobile{left:880px;width:300px}
section,header,footer{position:relative;overflow:hidden}
.abs{position:absolute}
.photo{position:absolute}
.brand{display:flex;align-items:center;gap:7px;color:#fff;font-family:"Cabin",sans-serif;font-weight:600;letter-spacing:.5px;text-transform:uppercase}
.brand .mark{width:14px;height:14px;border:2px solid #fff}
.brand span{line-height:1.05}
.btn{display:inline-flex;align-items:center;justify-content:center;background:var(--blue);color:#fff;font-family:"Montserrat",sans-serif;font-weight:700;text-transform:uppercase;letter-spacing:.4px}
.sec-title{font-family:"Montserrat",sans-serif;font-weight:700;text-align:center;text-transform:uppercase;color:var(--ink)}
.sec-title b{color:var(--blue);font-weight:700}
.divider{display:flex;align-items:center;justify-content:center;gap:8px;margin:6px auto 0}
.divider i{display:block;height:1px;background:var(--line)}
.divider u{display:block;width:11px;height:11px;border:1.5px solid var(--blue)}
.lorem{color:var(--muted)}
.hex{clip-path:polygon(50% 0,93% 25%,93% 75%,50% 100%,7% 75%,7% 25%);background:linear-gradient(#9a9da3,#7d8087);margin:0 auto}
.ghost{font-family:"Montserrat",sans-serif;font-weight:800;color:rgba(0,0,0,.05);white-space:nowrap;text-transform:uppercase}
.pager{display:flex;align-items:center;gap:6px;font-family:"Montserrat",sans-serif;font-weight:700;color:#fff}
.pager .pg{background:rgba(255,255,255,.25);color:#fff;display:flex;align-items:center;justify-content:center}
.pager .pg.on{background:#fff;color:var(--blue)}

/* ---------- desktop ---------- */
.d-hero{height:415px}
.d-hero .photo{inset:0;background:linear-gradient(180deg,#3c4a66 0%,#56627a 22%,#6d6a55 40%,#8a6f4f 58%,#a07f5c 72%,#5f6a44 86%,#3d4a36 100%)}
.d-nav{position:absolute;top:24px;left:157px;right:140px;display:flex;justify-content:space-between;align-items:center}
.d-nav .brand{font-size:11px}
.d-nav ul{display:flex;gap:13px;list-style:none;font-size:6.5px;color:#fff;font-weight:600;letter-spacing:.3px;text-transform:uppercase}
.d-hero .frame{position:absolute;left:157px;top:100px;width:235px;height:184px;border:2px solid rgba(255,255,255,.9);border-left:none;border-top:none}
.d-hero .frame::before{content:"";position:absolute;left:0;top:0;width:200px;height:2px;background:#fff}
.d-hero .frame::after{content:"";position:absolute;left:0;top:0;width:2px;height:184px;background:#fff}
.d-hero h1{position:absolute;left:176px;top:108px;color:#fff;font-weight:500;font-size:20px;line-height:1.25;text-transform:uppercase;letter-spacing:.3px}
.d-hero .intro{position:absolute;left:176px;top:172px;width:200px;font-size:7px;line-height:1.55;color:#eef}
.d-hero .btn{position:absolute;left:176px;top:258px;height:20px;padding:0 10px;font-size:7px}
.d-hero .pager{position:absolute;left:157px;top:320px;font-size:6px}
.d-hero .pager .pg{width:19px;height:19px;font-size:7px}
.d-hero .edge{position:absolute;left:0;bottom:0;width:820px;height:60px}

.d-about{height:281px;background:var(--mist)}
.d-about .ghost{position:absolute;left:175px;top:14px;font-size:86px}
.d-about h2{position:absolute;left:157px;top:40px;font-size:11px;font-weight:700;text-transform:uppercase}
.d-about p{position:absolute;left:157px;width:250px;font-size:6.6px;line-height:1.75}
.d-about .btn{position:absolute;left:157px;top:207px;width:74px;height:21px;font-size:5.6px}
.d-about .photo{left:445px;top:43px;width:215px;height:163px;background:linear-gradient(180deg,#5a6f98 0%,#3f4d6d 50%,#1a1d26 85%,#121418 100%)}
.d-about .rule{position:absolute;left:432px;top:60px;width:1px;height:150px;background:var(--line)}

.d-services{height:319px;background:#fff}
.d-services .tl{left:0;top:0;width:212px;height:205px;clip-path:polygon(0 0,100% 0,0 100%);background:linear-gradient(135deg,#4a64b4,#6d86c9 60%,#3a55a8)}
.d-services .br{right:0;bottom:0;width:140px;height:140px;clip-path:polygon(100% 0,100% 100%,0 100%);background:linear-gradient(315deg,#1f2228,#6a6d74 60%,#b9bcc2)}
.d-services .sec-title{position:absolute;left:0;right:0;top:42px;font-size:14px}
.d-services .divider{position:absolute;left:0;right:0;top:66px}
.d-services .divider i{width:90px}
.svc-row{position:absolute;left:220px;width:500px;top:100px;display:flex;justify-content:space-between}
.svc{width:160px;text-align:center}
.svc .hex{width:50px;height:56px}
.svc h3{font-size:11px;font-weight:600;margin-top:11px}
.svc p{font-size:6.4px;line-height:1.6;margin-top:7px}
.svc .btn{width:73px;height:18px;font-size:6.5px;margin-top:11px}

.d-proj-head{height:114px;background:var(--mist)}
.d-proj-head .sec-title{position:absolute;left:0;right:0;top:42px;font-size:14px}
.d-proj-head .divider{position:absolute;left:0;right:0;top:68px}
.d-proj-head .divider i{width:90px}
.d-projects{height:277px;display:flex}
.proj{position:relative;flex:1;height:100%}
.proj h4{position:absolute;left:15px;top:23px;color:#fff;font-family:"Montserrat",sans-serif;font-weight:600;font-size:10.5px;text-transform:uppercase;letter-spacing:.2px}
.proj small{position:absolute;left:15px;top:40px;color:rgba(255,255,255,.6);font-size:4.6px;font-weight:700;text-transform:uppercase;letter-spacing:.3px}
.proj .vert{position:absolute;left:13px;bottom:25px;transform-origin:left bottom;transform:rotate(-90deg) translate(0,8px);color:rgba(255,255,255,.55);font-size:5.4px;font-weight:600;text-transform:uppercase;white-space:nowrap;letter-spacing:.4px}
.proj .nav{position:absolute;top:137px;color:#fff;font-size:6px;font-weight:700;display:flex;gap:5px;align-items:center}

.d-news{height:383px;background:#fff}
.d-news .sec-title{position:absolute;left:0;right:0;top:36px;font-size:14px}
.d-news .divider{position:absolute;left:0;right:0;top:60px}
.d-news .divider i{width:90px}
.news-row{position:absolute;left:157px;top:108px;width:505px;display:flex;justify-content:space-between}
.news{width:158px;text-align:center}
.news .photo{position:relative;height:103px}
.news time{display:inline-block;background:#fff;color:var(--blue);font-size:6.5px;font-weight:600;padding:4px 14px;margin-top:-6px;position:relative}
.news h5{font-size:6.3px;font-weight:700;line-height:1.6;margin-top:8px;padding:0 14px}
.news p{font-size:5.6px;line-height:1.65;margin-top:6px;padding:0 12px}
.d-news .btn{position:absolute;left:357px;top:319px;width:104px;height:25px;font-size:6px}

.d-partners{height:183px;background:var(--mist)}
.d-partners .sec-title{position:absolute;left:0;right:0;top:38px;font-size:14px}
.d-partners .divider{position:absolute;left:0;right:0;top:62px}
.d-partners .divider i{width:90px}
.partners{position:absolute;left:130px;width:560px;top:100px;display:flex;justify-content:space-between;align-items:center}
.partners .arr{width:16px;height:16px;border:1px solid #9a9da4;border-radius:50%;display:flex;align-items:center;justify-content:center}
.partners .badge{background:#b7bac1}

.d-contact{height:249px;background:linear-gradient(180deg,#1d2029,#14161c)}
.d-contact h2{position:absolute;left:160px;top:40px;color:#fff;font-family:"Montserrat",sans-serif;font-weight:700;font-size:14px;letter-spacing:.3px}
.field{position:absolute;background:#2a2e39;color:#8a8f9b;font-size:4.6px;padding:4px 6px}
.d-contact .submit{position:absolute;left:604px;top:78px;width:60px;height:18px;font-size:5.5px}
.d-foot{position:absolute;left:160px;top:120px;width:505px;display:flex;justify-content:space-between}
.d-foot .badge{display:flex;flex-direction:column;align-items:center;gap:14px;width:50px}
.d-foot .badge .sq{width:30px;height:30px;border:3px solid var(--blue)}
.d-foot .dots{display:flex;gap:6px}
.d-foot .dots i{width:6px;height:6px;border-radius:50%;background:#4c5161}
.d-foot h6{color:#fff;font-size:4.8px;font-weight:700;text-transform:uppercase;margin-bottom:7px}
.d-foot li{list-style:none;color:#a6abb6;font-size:4.6px;line-height:2.1;text-transform:uppercase}
.d-foot .info li{text-transform:none;display:flex;gap:5px;align-items:center}
.d-foot .info li::before{content:"";width:4px;height:4px;border-radius:50%;background:var(--blue);flex:none}
.copy{position:absolute;left:0;right:0;bottom:14px;text-align:center;color:#7a7f8b;font-size:4.6px}

/* ---------- mobile ---------- */
.m-hero{height:225px;background:var(--mist)}
.m-hero .photo{left:0;top:0;width:300px;height:204px;background:linear-gradient(180deg,#3c4a66 0%,#5c6680 25%,#8a6f4f 55%,#a07f5c 72%,#55613f 100%)}
.m-hero .brand{position:absolute;left:16px;top:14px;font-size:11px}
.m-hero .menu{position:absolute;right:15px;top:15px;width:30px;height:26px;background:var(--blue);display:flex;flex-direction:column;justify-content:center;align-items:flex-end;gap:3px;padding-right:8px}
.m-hero .menu i{display:block;height:1.5px;background:#fff}
.m-hero .frame{position:absolute;left:16px;top:68px;width:132px;height:102px;border:1.5px solid #fff}
.m-hero h1{position:absolute;left:24px;top:72px;color:#fff;font-size:9.5px;font-weight:600;line-height:1.3;text-transform:uppercase}
.m-hero .intro{position:absolute;left:24px;top:100px;width:100px;font-size:6px;line-height:1.45;color:#fff}
.m-hero .btn{position:absolute;left:24px;top:139px;height:12px;padding:0 7px;font-size:4.6px}
.m-hero .pager{position:absolute;left:16px;top:178px;font-size:4.6px;gap:4px}
.m-hero .pager .pg{width:11px;height:11px;font-size:5px}
.m-hero .edge{position:absolute;left:0;top:180px;width:300px;height:45px}

.m-about{height:495px;background:var(--mist)}
.m-about .ghost{position:absolute;left:22px;top:2px;font-size:44px}
.m-about h2{position:absolute;left:0;right:0;top:18px;text-align:center;font-family:"Montserrat",sans-serif;font-size:17px;font-weight:700}
.m-about .rule{position:absolute;left:16px;top:79px;width:1px;height:180px;background:var(--line)}
.m-about .photo{left:29px;top:66px;width:256px;height:193px;background:linear-gradient(180deg,#56698f 0%,#3f4d6d 50%,#1a1d26 85%,#121418 100%)}
.m-about p{position:absolute;left:14px;top:285px;width:270px;font-size:9.6px;line-height:1.95;color:#444a56}
.m-about .btn{position:absolute;left:14px;top:441px;width:107px;height:31px;font-size:8px}

.m-services{height:997px;background:#fff}
.m-services .tl{left:0;top:0;width:100px;height:100px;clip-path:polygon(0 0,100% 0,0 100%);background:linear-gradient(135deg,#4a64b4,#7b92cf 60%,#3a55a8)}
.m-services .br{right:0;bottom:0;width:105px;height:105px;clip-path:polygon(100% 0,100% 100%,0 100%);background:linear-gradient(315deg,#1f2228,#6a6d74 60%,#b9bcc2)}
.m-services .sec-title{position:absolute;left:0;right:0;top:32px;font-size:18px;padding-left:10px}
.m-services .divider{position:absolute;left:0;right:0;top:62px}
.m-services .divider i{width:95px}
.m-svc{position:absolute;left:20px;width:260px;text-align:center}
.m-svc .hex{width:74px;height:82px}
.m-svc h3{font-size:17px;font-weight:600;margin-top:22px}
.m-svc p{font-size:9.6px;line-height:1.6;margin-top:14px;padding:0 8px}
.m-svc .btn{width:106px;height:28px;font-size:10px;margin-top:20px}

.m-proj-head{height:106px;background:var(--mist)}
.m-proj-head .sec-title{position:absolute;left:0;right:0;top:32px;font-size:18px}
.m-proj-head .divider{position:absolute;left:0;right:0;top:62px}
.m-proj-head .divider i{width:95px}
.m-project{height:405px}
.m-project h4{position:absolute;left:22px;top:43px;color:#fff;font-family:"Montserrat",sans-serif;font-weight:600;font-size:16px;text-transform:uppercase}
.m-project small{position:absolute;left:22px;top:66px;color:rgba(255,255,255,.6);font-size:6.4px;font-weight:700;text-transform:uppercase}
.m-project .vert{position:absolute;left:24px;bottom:30px;transform-origin:left bottom;transform:rotate(-90deg) translate(0,10px);color:rgba(255,255,255,.6);font-size:8.5px;font-weight:600;text-transform:uppercase;white-space:nowrap;letter-spacing:.5px}
.m-project .nav{position:absolute;top:217px;color:#fff;font-size:8.5px;font-weight:700;display:flex;gap:8px;align-items:center}
</style>
</head>
<body>

<!-- ================= DESKTOP ================= -->
<main class="site site-desktop" aria-label="Desktop home page">

  <header class="d-hero">
    <div class="photo" role="img" aria-label="Aerial photo of a channel construction site with excavators beside a residential neighbourhood"></div>
    <nav class="d-nav">
      <div class="brand"><i class="mark"></i><span>Harlow Stonefield</span></div>
      <ul><li>Home</li><li>Project Gallery</li><li>Employment Application</li><li>Contact Us</li></ul>
    </nav>
    <div class="frame"></div>
    <h1>Harlow Stonefield<br>Civil Construction</h1>
    <p class="intro">Lorem ipsum dolor sit amet, consectetur adipiscing elit. Donec ut finibus enim. Donec sollicitudin turpis justo, sit amet porttitor lorem dictum sit amet. Integer vel tincidunt purus. Aliquam maximus lacus nec lorem accumsan blandit. Mauris eleifend, eros et mollis commodo, nisl metus finibus nibh, ac tempus dolor ipsum eu felis.</p>
    <a class="btn">Learn More &nbsp;→</a>
    <div class="pager"><span class="pg on">1</span><span class="pg">2</span><span class="pg">3</span><span>&nbsp;←&nbsp; PREV</span><span>NEXT &nbsp;→</span></div>
    <svg class="edge" viewBox="0 0 820 60" preserveAspectRatio="none">
      <polygon points="0,0 410,36 820,0 820,60 0,60" fill="#3a55a8"/>
      <polygon points="0,2 410,30 820,-6 820,8 410,44 0,14" fill="#3a55a8"/>
      <polygon points="0,0 410,30 820,-4 820,60 0,60" fill="#f2f2f3" transform="translate(0,6)"/>
    </svg>
  </header>

  <section class="d-about">
    <div class="ghost">About Us</div>
    <h2>About Us</h2>
    <p style="top:60px">Lorem ipsum dolor sit amet, consectetur adipiscing elit. Donec ut finibus enim. Donec sollicitudin turpis justo, sit amet porttitor lorem dictum sit amet. Integer vel tincidunt purus. Aliquam maximus lacus nec lorem accumsan blandit. Mauris eleifend, eros et mollis commodo, nisl metus finibus nibh, ac tempus dolor ipsum eu felis.</p>
    <p style="top:152px">Morbi lacus enim, blandit quis interdum eu, rutrum vel massa. Suspendisse mollis mattis faucibus. Nunc luctus sem quis vehicula iaculis.</p>
    <a class="btn">Read More</a>
    <div class="rule"></div>
    <div class="photo" role="img" aria-label="Dusk silhouette of an excavator at work with the company name overlaid"></div>
    <div class="brand abs" style="left:490px;top:118px;font-size:11px"><i class="mark"></i><span>Harlow Stonefield<br><small style="font-size:7px;font-weight:400;letter-spacing:2px">Civil Construction</small></span></div>
  </section>

  <section class="d-services">
    <div class="photo tl" role="img" aria-label="Blue-toned photo of an excavator arm"></div>
    <div class="photo br" role="img" aria-label="Greyscale photo of heavy machinery on site"></div>
    <h2 class="sec-title">Our <b>Services</b></h2>
    <div class="divider"><i></i><u></u><i></i></div>
    <div class="svc-row">
      <div class="svc"><div class="hex" role="img" aria-label="Channel stabilization icon"></div><h3>Channel Stabilization</h3><p class="lorem">Lorem ipsum dolor sit amet, consectetur adipiscing elit. Donec ut finibus enim. Donec sollicitudin turpis justo, sit amet porttitor lorem dictum sit amet. Integer vel tincidunt purus. Aliquam maximus lacus nec lorem accumsan blandit.</p><a class="btn">Read More</a></div>
      <div class="svc"><div class="hex" role="img" aria-label="Excavation and grading icon"></div><h3>Excavation and Grading</h3><p class="lorem">Lorem ipsum dolor sit amet, consectetur adipiscing elit. Donec ut finibus enim. Donec sollicitudin turpis justo, sit amet porttitor lorem dictum sit amet. Integer vel tincidunt purus. Aliquam maximus lacus nec lorem accumsan blandit.</p><a class="btn">Read More</a></div>
      <div class="svc"><div class="hex" role="img" aria-label="Underground utilities icon"></div><h3>Underground Utilities</h3><p class="lorem">Lorem ipsum dolor sit amet, consectetur adipiscing elit. Donec ut finibus enim. Donec sollicitudin turpis justo, sit amet porttitor lorem dictum sit amet. Integer vel tincidunt purus. Aliquam maximus lacus nec lorem accumsan blandit.</p><a class="btn">Read More</a></div>
    </div>
  </section>

  <section class="d-proj-head">
    <h2 class="sec-title">Our <b>Projects</b></h2>
    <div class="divider"><i></i><u></u><i></i></div>
  </section>

  <section class="d-projects">
    <div class="proj" role="img" aria-label="Blue-tinted photo of a concrete culvert being installed" style="background:linear-gradient(180deg,#4560b0,#2e4590 55%,#233a7e)">
      <h4>Underground Utilities</h4><small>Harlow Stonefield Civil Construction</small>
      <span class="vert">Harlow Stonefield Civil Construction</span>
      <span class="nav" style="left:48px">← &nbsp;PREV</span>
    </div>
    <div class="proj" role="img" aria-label="Grey-tinted aerial photo of a straight concrete channel" style="background:linear-gradient(180deg,#9297a3,#7d8391 60%,#6c7381)">
      <h4>Channel Stabilization</h4><small>Harlow Stonefield Civil Construction</small>
      <span class="vert">Harlow Stonefield Civil Construction</span>
    </div>
    <div class="proj" role="img" aria-label="Blue-tinted photo of an excavator with palm trees" style="background:linear-gradient(180deg,#4a64b3,#34509f 60%,#2a4390)">
      <h4>Excavation and Grading</h4><small>Harlow Stonefield Civil Construction</small>
      <span class="vert">Harlow Stonefield Civil Construction</span>
    </div>
    <div class="proj" role="img" aria-label="Grey-tinted aerial photo of a land development" style="background:linear-gradient(180deg,#9aa0ab,#878d99 60%,#737a87)">
      <h4>Land Development</h4><small>Harlow Stonefield Civil Construction</small>
      <span class="vert">Harlow Stonefield Civil Construction</span>
      <span class="nav" style="left:110px">NEXT&nbsp; →</span>
    </div>
  </section>

  <section class="d-news">
    <h2 class="sec-title">Latest <b>News</b></h2>
    <div class="divider"><i></i><u></u><i></i></div>
    <div class="news-row">
      <article class="news"><div class="photo" role="img" aria-label="Photo of a drainage channel under a blue sky" style="background:linear-gradient(180deg,#6f8fc4,#3d5a86 50%,#2b3b4f)"></div><time>Jun 10, 2019</time><h5>Morbi vel nisl purus. In varius dignissim ligula quis accumsan quam</h5><p class="lorem">Lorem ipsum dolor sit amet, consectetur adipiscing elit. Donec ut finibus enim. Donec sollicitudin turpis justo, sit amet porttitor lorem dictum sit amet.</p></article>
      <article class="news"><div class="photo" role="img" aria-label="Photo of a freshly seeded green embankment" style="background:linear-gradient(180deg,#6d7d5a,#3f7a55 55%,#2f9a7a)"></div><time>May 27, 2019</time><h5>Morbi vel nisl purus. In varius dignissim ligula quis accumsan quam</h5><p class="lorem">Lorem ipsum dolor sit amet, consectetur adipiscing elit. Donec ut finibus enim. Donec sollicitudin turpis justo, sit amet porttitor lorem dictum sit amet.</p></article>
      <article class="news"><div class="photo" role="img" aria-label="Photo of a pipe trench with a yellow excavator" style="background:linear-gradient(180deg,#c9a25a,#a07a3e 55%,#6d5432)"></div><time>May 20, 2019</time><h5>Morbi vel nisl purus. In varius dignissim ligula quis accumsan quam</h5><p class="lorem">Lorem ipsum dolor sit amet, consectetur adipiscing elit. Donec ut finibus enim. Donec sollicitudin turpis justo, sit amet porttitor lorem dictum sit amet.</p></article>
    </div>
    <a class="btn">View More Blog</a>
  </section>

  <section class="d-partners">
    <h2 class="sec-title">Our <b>Partners</b></h2>
    <div class="divider"><i></i><u></u><i></i></div>
    <div class="partners">
      <span class="arr"><svg width="8" height="8" viewBox="0 0 8 8"><path d="M5 1 2 4l3 3" fill="none" stroke="#7a7e86" stroke-width="1"/></svg></span>
      <span class="badge" style="width:64px;height:26px"></span>
      <span class="badge" style="width:34px;height:34px;border-radius:50%"></span>
      <span class="badge" style="width:64px;height:26px"></span>
      <span class="badge" style="width:34px;height:34px;border-radius:50%"></span>
      <span class="badge" style="width:34px;height:34px"></span>
      <span class="arr"><svg width="8" height="8" viewBox="0 0 8 8"><path d="M3 1l3 3-3 3" fill="none" stroke="#7a7e86" stroke-width="1"/></svg></span>
    </div>
  </section>

  <footer class="d-contact">
    <h2>CONTACT US</h2>
    <span class="field" style="left:318px;top:30px;width:96px;height:18px">First Name</span>
    <span class="field" style="left:418px;top:30px;width:96px;height:18px">Last Name</span>
    <span class="field" style="left:518px;top:30px;width:146px;height:42px">Message</span>
    <span class="field" style="left:318px;top:52px;width:96px;height:18px">Phone</span>
    <span class="field" style="left:418px;top:52px;width:96px;height:18px">Email</span>
    <a class="btn submit">Submit Now!</a>
    <div class="d-foot">
      <div class="badge"><span class="sq"></span><span class="dots"><i></i><i></i><i></i><i></i></span></div>
      <div><h6>Quick Links</h6><ul><li>Home</li><li>About Us</li><li>Gallery</li><li>Contact Us</li></ul></div>
      <div><h6>Services</h6><ul><li>Channel Stabilization</li><li>Underground Utilities</li><li>Excavation and Grading</li><li>Land Development</li></ul></div>
      <div><h6>Explore Us</h6><ul><li>Support</li><li>FAQ</li><li>Client Feedback</li><li>Privacy Policy</li></ul></div>
      <div class="info"><h6>Contact Info</h6><ul><li>1420 Quarry Lane, Suite 5,<br>Brookfield Valley</li><li>(000) 123 456 7890</li><li>(000) 123 456 7891</li><li>hello@harlowstonefieldcivil.com</li></ul></div>
    </div>
    <p class="copy">Copyright © 2019 Harlow Stonefield Civil Construction. All rights reserved.</p>
  </footer>
</main>

<!-- ================= MOBILE ================= -->
<main class="site site-mobile" aria-label="Mobile home page">

  <header class="m-hero">
    <div class="photo" role="img" aria-label="Aerial photo of a channel construction site with excavators"></div>
    <div class="brand"><i class="mark"></i><span>Harlow Stonefield</span></div>
    <span class="menu"><i style="width:14px"></i><i style="width:10px"></i><i style="width:14px"></i></span>
    <div class="frame"></div>
    <h1>Harlow Stonefield<br>Civil Construction</h1>
    <p class="intro">Lorem ipsum dolor sit amet, consectetur adipiscing elit. Donec ut finibus enim.</p>
    <a class="btn">Learn More &nbsp;→</a>
    <div class="pager"><span class="pg on">1</span><span class="pg">2</span><span class="pg">3</span><span>← PREV</span><span>NEXT →</span></div>
    <svg class="edge" viewBox="0 0 300 45" preserveAspectRatio="none">
      <polygon points="0,24 150,8 300,24 300,14 150,0 0,14" fill="#3a55a8"/>
      <polygon points="0,24 150,10 300,24 300,45 0,45" fill="#f2f2f3"/>
    </svg>
  </header>

  <section class="m-about">
    <div class="ghost">About Us</div>
    <h2>ABOUT US</h2>
    <div class="rule"></div>
    <div class="photo" role="img" aria-label="Dusk silhouette of an excavator at work with the company name overlaid"></div>
    <div class="brand abs" style="left:60px;top:150px;font-size:13px"><i class="mark"></i><span>Harlow Stonefield<br><small style="font-size:8px;font-weight:400;letter-spacing:2px">Civil Construction</small></span></div>
    <p>Lorem ipsum dolor sit amet, consectetur adipiscing elit. Donec ut finibus enim. Donec sollicitudin turpis justo, sit amet porttitor lorem dictum sit amet. Integer vel tincidunt purus. Aliquam maximus lacus nec lorem accumsan blandit. Mauris eleifend, eros et mollis commodo, nisl metus finibus nibh, ac tempus dolor ipsum eu felis. iaculis.</p>
    <a class="btn">Read More</a>
  </section>

  <section class="m-services">
    <div class="photo tl" role="img" aria-label="Blue-toned photo of an excavator arm"></div>
    <div class="photo br" role="img" aria-label="Greyscale photo of heavy machinery on site"></div>
    <h2 class="sec-title">Our <b>Services</b></h2>
    <div class="divider"><i></i><u></u><i></i></div>
    <div class="m-svc" style="top:100px"><div class="hex" role="img" aria-label="Channel stabilization icon"></div><h3>Channel Stabilization</h3><p class="lorem">Lorem ipsum dolor sit amet, consectetur adipiscing elit. Donec ut finibus enim. Donec sollicitudin turpis justo, sit amet porttitor lorem dictum sit amet. Integer vel tincidunt purus. Aliquam maximus lacus nec lorem accumsan blandit.</p><a class="btn">Read More</a></div>
    <div class="m-svc" style="top:384px"><div class="hex" role="img" aria-label="Excavation and grading icon"></div><h3>Excavation and Grading</h3><p class="lorem">Lorem ipsum dolor sit amet, consectetur adipiscing elit. Donec ut finibus enim. Donec sollicitudin turpis justo, sit amet porttitor lorem dictum sit amet. Integer vel tincidunt purus. Aliquam maximus lacus nec lorem accumsan blandit.</p><a class="btn">Read More</a></div>
    <div class="m-svc" style="top:670px"><div class="hex" role="img" aria-label="Underground utilities icon"></div><h3>Underground Utilities</h3><p class="lorem">Lorem ipsum dolor sit amet, consectetur adipiscing elit. Donec ut finibus enim. Donec sollicitudin turpis justo, sit amet porttitor lorem dictum sit amet. Integer vel tincidunt purus. Aliquam maximus lacus nec lorem accumsan blandit.</p><a class="btn">Read More</a></div>
  </section>

  <section class="m-proj-head">
    <h2 class="sec-title">Our <b>Projects</b></h2>
    <div class="divider"><i></i><u></u><i></i></div>
  </section>

  <section class="m-project" role="img" aria-label="Blue-tinted photo of a concrete culvert being installed" style="background:linear-gradient(180deg,#4560b0,#2e4590 55%,#233a7e)">
    <h4>Underground Utilities</h4><small>Harlow Stonefield Civil Construction</small>
    <span class="vert">Harlow Stonefield Civil Construction</span>
    <span class="nav" style="left:52px">← &nbsp;PREV</span>
    <span class="nav" style="left:195px">NEXT &nbsp;→</span>
  </section>
</main>

</body>
</html>
```